Talbern Learning Recruitment Business Cards

We need business cards designed for our growing recruitment business.
We have just launched our offices in Sydney Melbourne and have a well established business in Perth. We are a fun young firm that specialise in Early Years Education Recruitment.
Our vision mission values are below
Our Vision:
To be:
the single, nationally recognised leader in the Early Childhood Sector.
a multifaceted organisation with a network of expertly driven facilities in the Early Childhood Sector, acknowledged as an organisation of integrity, innovation, heart and community.

Our Mission:
To provide superior quality recruitment services and solutions to the Early Childhood sector.
We empower our candidates to succeed.
We engage in trusted partnerships with our clients.
We grow our business/network/community, with passion and integrity.

Our Values:

We… are REAL
think: CUSTOMER
find: SOLUTIONS
achieve: RESULTS
enjoy: WHAT WE DO

Our website is www.talbernlearning.com feel free to visit it for inspiration.
Name Felix Ormsby
Title National Director
1300 057 812
0462 315 706
felix@talbernstaffing.com
website www.talbernlearning.com

I have attached our current business cards and logo designs to view

Target Market(s)

Recruitment

Industry/Entity Type

Business

Contact Information for Business Card

Name Felix Ormsby
Title National Director
1300 057 812
0462 315 706

Font styles to use
Serif

Requirements
Must have
• Company Values and the cities we have offices in Perth | Sydney | Melbourne
Nice to have
• Our Vision on the card
• Our Vision:
• To be a nationally recognised leader in the Early Childhood Sector.
• A multifaceted organisation with a network of expertly driven facilities in the Early Childhood Sector, acknowledged as an organisation of integrity, innovation, heart and community.

```html
<!DOCTYPE html>
<html lang="en">
<head>
<meta charset="utf-8">
<title>Talbern Learning Recruitment – Business Cards</title>
<link rel="stylesheet" href="https://fonts.googleapis.com/css2?family=Lora:wght@400;500;600;700&display=swap">
<style>
  :root {
    --page-bg: #ecebe8;
    --card-top: #e6f3fd;
    --card-mid: #c4e2f7;
    --card-deep: #0b78c2;
    --navy: #1b4f86;
    --cyan: #1f9bd8;
    --band: #3458a8;
    --white: #ffffff;
    --shadow: rgba(40, 50, 70, 0.22);
  }
  * { box-sizing: border-box; margin: 0; padding: 0; }
  html, body { width: 1200px; height: 872px; overflow: hidden; }
  body {
    background: var(--page-bg);
    font-family: "Lora", Georgia, serif;
    position: relative;
  }
  .card {
    position: absolute;
    width: 540px;
    height: 310px;
    border-radius: 14px;
    overflow: hidden;
    box-shadow: 0 10px 28px var(--shadow);
  }

  /* Front */
  .card-front {
    left: 60px; top: 80px;
    background: linear-gradient(180deg, var(--card-top) 0%, var(--card-mid) 55%, var(--card-deep) 100%);
  }
  .front-brand {
    position: absolute; left: 44px; top: 70px;
    display: flex; align-items: center; gap: 22px;
  }
  .brand-circle {
    width: 120px; height: 120px; border-radius: 50%;
    border: 3px solid var(--navy);
    flex: none;
  }
  .front-name {
    font-weight: 500; font-size: 30px; letter-spacing: 1px;
    color: var(--navy); line-height: 1.1; white-space: nowrap;
  }
  .front-tagline {
    font-size: 15px; font-weight: 600; color: var(--navy); margin-top: 8px; white-space: nowrap;
  }
  .front-tagline span { color: var(--cyan); font-weight: 400; }
  .values {
    position: absolute; left: 20px; right: 20px; bottom: 18px;
    list-style: none;
    display: flex; flex-wrap: wrap; justify-content: center; gap: 4px 16px;
    color: var(--white); font-size: 11.5px; line-height: 1.3;
  }
  .value strong { font-weight: 700; letter-spacing: .5px; }

  /* Back */
  .card-back {
    left: 600px; top: 480px;
    background: linear-gradient(180deg, var(--card-top) 0%, #d3eafa 70%, #7bbde6 90%, var(--card-deep) 100%);
  }
  .map-area {
    position: absolute; left: 240px; top: 40px; width: 260px; height: 230px;
    border-radius: 40% 50% 45% 40%;
    background: radial-gradient(ellipse at center, rgba(170, 205, 232, 0.35), rgba(170, 205, 232, 0) 70%);
  }
  .back-brand {
    position: absolute; left: 24px; top: 24px;
    display: flex; align-items: center; gap: 8px;
  }
  .back-brand .brand-circle { width: 62px; height: 62px; border-width: 2px; }
  .back-name {
    font-weight: 600; font-size: 13px; letter-spacing: .5px; color: var(--navy); line-height: 1.3;
  }
  .back-tagline {
    position: absolute; left: 24px; top: 92px;
    font-size: 8px; font-weight: 600; color: var(--navy); white-space: nowrap;
  }
  .person { position: absolute; right: 60px; top: 90px; }
  .person-name { font-weight: 700; font-size: 25px; color: var(--navy); line-height: 1.15; white-space: nowrap; }
  .person-title { font-size: 14px; color: var(--cyan); margin-left: 22px; }

  .offices { position: absolute; left: 0; top: 178px; list-style: none; }
  .office {
    display: flex; align-items: center; justify-content: space-between;
    width: 118px; height: 22px; margin-bottom: 6px;
    background: var(--band); color: var(--white);
    font-size: 12px; padding-left: 12px;
    border-radius: 0 12px 12px 0;
  }
  .icon-dot {
    width: 20px; height: 20px; border-radius: 50%;
    background: var(--white); border: 2px solid var(--band);
    display: flex; align-items: center; justify-content: center; flex: none;
  }
  .contacts { position: absolute; right: 0; top: 200px; list-style: none; }
  .contact {
    display: flex; align-items: center; justify-content: flex-end;
    height: 24px; margin-bottom: 8px;
    font-size: 12.5px; color: var(--navy);
  }
  .contact-text { text-align: right; line-height: 1.15; margin-right: 8px; white-space: nowrap; }
  .contact-band {
    width: 96px; height: 22px; background: var(--band);
    display: flex; align-items: center; padding-left: 4px;
    border-radius: 12px 0 0 12px;
  }
  .contact-phone { height: 34px; }
</style>
</head>
<body>

<section class="card card-front" aria-label="Business card front">
  <div class="front-brand">
    <div class="brand-circle"></div>
    <div>
      <div class="front-name">TALBERN LEARNING</div>
      <div class="front-tagline">Bringing quality to <span>education recruitment</span></div>
    </div>
  </div>
  <ul class="values" aria-label="Company values">
    <li class="value">We… are <strong>REAL</strong></li>
    <li class="value">think: <strong>CUSTOMER</strong></li>
    <li class="value">find: <strong>SOLUTIONS</strong></li>
    <li class="value">achieve: <strong>RESULTS</strong></li>
    <li class="value">enjoy: <strong>WHAT WE DO</strong></li>
  </ul>
</section>

<section class="card card-back" aria-label="Business card back">
  <div class="map-area" role="img" aria-label="Faint map of Australia with office location pins"></div>

  <div class="back-brand">
    <div class="brand-circle"></div>
    <div class="back-name">TALBERN<br>LEARNING</div>
  </div>
  <div class="back-tagline">Bringing quality to education recruitment</div>

  <div class="person">
    <div class="person-name">Felix Ormsby</div>
    <div class="person-title">National Director</div>
  </div>

  <ul class="offices">
    <li class="office">Perth <span class="icon-dot"><svg width="10" height="12" viewBox="0 0 10 12"><path d="M5 0a4 4 0 0 0-4 4c0 3 4 8 4 8s4-5 4-8a4 4 0 0 0-4-4z" fill="#1f9bd8"/><circle cx="5" cy="4" r="1.5" fill="#fff"/></svg></span></li>
    <li class="office">Sydney <span class="icon-dot"><svg width="10" height="12" viewBox="0 0 10 12"><path d="M5 0a4 4 0 0 0-4 4c0 3 4 8 4 8s4-5 4-8a4 4 0 0 0-4-4z" fill="#1f9bd8"/><circle cx="5" cy="4" r="1.5" fill="#fff"/></svg></span></li>
    <li class="office">Melbourne <span class="icon-dot"><svg width="10" height="12" viewBox="0 0 10 12"><path d="M5 0a4 4 0 0 0-4 4c0 3 4 8 4 8s4-5 4-8a4 4 0 0 0-4-4z" fill="#1f9bd8"/><circle cx="5" cy="4" r="1.5" fill="#fff"/></svg></span></li>
  </ul>

  <ul class="contacts">
    <li class="contact contact-phone">
      <span class="contact-text">1300 057 812<br>0462 315 706</span>
      <span class="contact-band"><span class="icon-dot"><svg width="10" height="10" viewBox="0 0 10 10"><path d="M2 0.5l2 2-1 1.2c.6 1.3 1.5 2.2 2.8 2.8L7 5.5l2 2-1.2 1.8C4 9 1 6 .6 1.8z" fill="#1f9bd8"/></svg></span></span>
    </li>
    <li class="contact">
      <span class="contact-text">felix@talbernstaffing.com</span>
      <span class="contact-band"><span class="icon-dot"><svg width="11" height="8" viewBox="0 0 11 8"><rect x=".5" y=".5" width="10" height="7" fill="#1f9bd8"/><path d="M.5 .5l5 4 5-4" stroke="#fff" fill="none"/></svg></span></span>
    </li>
    <li class="contact">
      <span class="contact-text">www.talbernlearning.com</span>
      <span class="contact-band"><span class="icon-dot"><svg width="11" height="11" viewBox="0 0 12 12"><circle cx="6" cy="6" r="5" fill="none" stroke="#1f9bd8" stroke-width="1.2"/><ellipse cx="6" cy="6" rx="2.2" ry="5" fill="none" stroke="#1f9bd8"/><path d="M1 6h10M2 3.5h8M2 8.5h8" stroke="#1f9bd8" stroke-width=".8"/></svg></span></span>
    </li>
  </ul>
</section>

</body>
</html>
```